Communication and Marketing agency needs a new presentation card

We are a group of communication and marketing agencies specialized in companies that are in the logistics and industrial sector. The head agency is TELVANO Grupo and the group consists of 4 agencies: TELVANO Media, TELVANO Digital, TELVANO Research and EnlazaPorImagen. We hace 4 offices in Spain (Madrid, Barcelona, Valencia and Murcia). We are looking for a clean and attractive design that transmits our experience, brand presence in the market and knowledge to those who receive the card.It has to maintain the colors of the logo that is attached.
Target Market(s)
logistics and industrial sector
Marketing department
Clean and attractive design

```html
<!DOCTYPE html>
<html lang="en">
<head>
<meta charset="utf-8">
<title>TELVANO Grupo — Business Card</title>
<link rel="stylesheet" href="https://fonts.googleapis.com/css2?family=Open+Sans:wght@400;600&display=swap">
<style>
  :root {
    --brand-red: #b51f2e;
    --brand-dark: #2b2726;
    --ink: #1f1f1f;
    --grey: #555050;
    --paper: #ffffff;
    --backdrop: #dfe3e8;
  }
  * { margin: 0; padding: 0; box-sizing: border-box; }
  html, body {
    width: 1200px; height: 1200px; overflow: hidden;
    background: var(--backdrop);
    font-family: "Open Sans", Arial, sans-serif;
  }
  .sheet {
    width: 1200px; height: 1200px;
    display: flex; flex-direction: column; align-items: center; justify-content: center;
    gap: 60px;
  }
  .card {
    position: relative;
    width: 875px; height: 500px;
    background: var(--paper);
    box-shadow: 0 2px 10px rgba(0,0,0,0.12);
    overflow: hidden;
  }
  .card__band { position: absolute; left: 0; bottom: 0; width: 875px; height: 22px; }

  /* Back side */
  .brand-main {
    position: absolute; left: 0; right: 0; top: 150px;
    text-align: center;
    color: var(--brand-red);
    font-weight: 600; font-size: 70px; letter-spacing: 3px; line-height: 1;
    white-space: nowrap;
  }
  .agency-row {
    position: absolute; left: 50px; right: 50px; top: 330px;
    display: flex; justify-content: space-between; align-items: center;
    gap: 28px;
  }
  .agency {
    font-weight: 600; font-size: 18px; letter-spacing: 0.5px;
    white-space: nowrap;
  }
  .agency--red { color: var(--brand-red); }
  .agency--grey { color: var(--grey); }

  /* Front side */
  .brand-front {
    position: absolute; left: 44px; top: 60px;
    color: var(--brand-red);
    font-weight: 600; font-size: 60px; letter-spacing: 3px; line-height: 1;
    white-space: nowrap;
  }
  .holder {
    position: absolute; right: 330px; top: 320px;
    text-align: right;
  }
  .holder__name { color: var(--brand-red); font-size: 34px; font-weight: 400; line-height: 1.1; white-space: nowrap; }
  .holder__role { color: var(--ink); font-size: 20px; margin-top: 4px; }
  .divider {
    position: absolute; left: 560px; top: 280px; width: 1.5px; height: 160px;
    background: var(--brand-red);
  }
  .contact {
    position: absolute; left: 580px; top: 278px;
    color: var(--ink); font-size: 19px; line-height: 1.5; letter-spacing: 0.5px;
    white-space: nowrap;
  }
  .contact__address { margin-top: 12px; }
</style>
</head>
<body>
<main class="sheet">

  <section class="card card--back" aria-label="Card back">
    <div class="brand-main">TELVANO Grupo</div>
    <div class="agency-row">
      <span class="agency agency--grey">TELVANO Digital</span>
      <span class="agency agency--grey">TELVANO Research</span>
      <span class="agency agency--red">TELVANO Media</span>
      <span class="agency agency--red">EnlazaPorImagen</span>
    </div>
    <svg class="card__band" viewBox="0 0 875 22" aria-hidden="true">
      <polygon points="0,8 540,8 528,22 0,22" fill="var(--brand-red)"/>
      <polygon points="552,4 875,4 875,22 540,22" fill="var(--brand-dark)"/>
    </svg>
  </section>

  <section class="card card--front" aria-label="Card front">
    <div class="brand-front">TELVANO Grupo</div>
    <div class="holder">
      <div class="holder__name">LUCAS FERRER</div>
      <div class="holder__role">Director</div>
    </div>
    <div class="divider"></div>
    <div class="contact">
      <div>+34 611 482 905</div>
      <div>lucas@telvanogrupo.com</div>
      <div>www.telvanogrupo.com</div>
      <div class="contact__address">Calle Ribera 14<br>Valencia, Spain</div>
    </div>
    <svg class="card__band" viewBox="0 0 875 22" aria-hidden="true">
      <polygon points="0,8 540,8 528,22 0,22" fill="var(--brand-red)"/>
      <polygon points="552,4 875,4 875,22 540,22" fill="var(--brand-dark)"/>
    </svg>
  </section>

</main>
</body>
</html>
```